Recital Flyer - Step Into Starlight

I need a flyer to depict a contemporary recital theme, "Step Into Starlight..." for my 6th Annual Recital. I am looking for a Velmont Plaza "look" that is set in Detroit or has a "Detroit" Influence.

Here are some of the featured plays we are using: Ghost in the Ballroom, Glitterbug, A Kettle Waltz, The Otter Queen, The Tinted Meadow, Slipper Bash, Tamberly, Kick Up Tha Beat/Kick Up Tha Soul, Rivetline The Revue, Tapworth, Glint and more!
Updates

hi there I would like to add a $75 tip, how do I do that?

Target Market(s)

Dancers - students ages 3-15

Industry/Entity Type

Dance Studio

Font styles to use
Other font styles liked:
• Broadway or something familiar

Requirements
Must have
• My Logo and pertinent information on it:
• Date: June 24, 2017
• Time: 2 PM & 7 PM
• Location: Pinecrest Hollow High School
• 418 Marlow Rd, Ashford Charter Twp, MI 48612
Nice to have
• A New York (Velmont Plaza) flair with a gritty Detroit Influnce!

```html
<!DOCTYPE html>
<html lang="en">
<head>
<meta charset="utf-8">
<title>Step Into Starlight – 6th Annual Recital</title>
<link rel="stylesheet" href="https://fonts.googleapis.com/css2?family=Cinzel:wght@400;700;900&display=swap">
<style>
  :root {
    --backdrop: #3a3a3b;
    --maroon: #72163b;
    --teal: #137880;
    --gold: #f2e406;
    --white: #ffffff;
    --paper-edge: #c9c9cb;
    --paper-mid: #ffffff;
    --pink: #e8388c;
    --sky: #5ec4d4;
  }
  * { margin: 0; padding: 0; box-sizing: border-box; }
  html, body {
    width: 1200px; height: 1200px; overflow: hidden;
    background: var(--backdrop);
    font-family: "Cinzel", Georgia, serif;
  }
  .flyer {
    position: absolute; left: 96px; top: 264px;
    width: 1008px; height: 672px;
    background: linear-gradient(90deg, var(--paper-edge) 0%, var(--paper-mid) 22%, var(--paper-mid) 78%, var(--paper-edge) 100%);
    box-shadow: 4px 6px 10px rgba(0,0,0,.45);
    overflow: hidden;
  }
  .studio-name {
    position: absolute; left: 0; width: 1004px; top: 84px;
    text-align: center; color: var(--maroon);
    font-weight: 700; font-size: 24px; letter-spacing: 1.5px;
  }
  .theme-title {
    position: absolute; left: 44px; top: 160px; z-index: 1;
    color: var(--maroon); font-weight: 700;
    font-size: 36px; letter-spacing: 6px; white-space: nowrap;
  }
  .title-band {
    position: absolute; left: 0; top: 217px; width: 100%; height: 111px;
    background: var(--maroon);
  }
  .title-rule {
    position: absolute; left: 0; top: 334px; width: 100%; height: 6px;
    background: var(--maroon);
  }
  .recital-line {
    position: absolute; left: 46px; top: 242px;
    color: var(--white); font-weight: 700; font-size: 30px; white-space: nowrap;
  }
  .recital-line .edition {
    color: var(--gold); font-size: 50px; font-weight: 900; vertical-align: -4px;
  }
  .details {
    position: absolute; left: 73px; top: 376px;
    border-left: 2px solid var(--maroon);
    padding: 20px 0 22px 19px;
    color: var(--maroon); font-weight: 700; font-size: 29px; line-height: 48px;
  }
  .venue-rule {
    position: absolute; left: 0; top: 551px; width: 100%; height: 8px;
    background: var(--teal);
  }
  .venue-band {
    position: absolute; left: 0; top: 566px; width: 100%; height: 106px;
    background: var(--teal); color: var(--white);
    text-align: center; font-weight: 700;
  }
  .venue-name { font-size: 23px; margin-top: 21px; letter-spacing: .5px; }
  .venue-address { font-size: 19px; margin-top: 12px; }
  .dancer-art {
    position: absolute; left: 640px; top: 122px; width: 350px; height: 446px;
    border-radius: 50% 42% 34% 30% / 40% 40% 30% 34%;
    background:
      radial-gradient(circle at 70% 30%, var(--pink) 0%, rgba(232,56,140,.6) 35%, transparent 60%),
      radial-gradient(circle at 40% 70%, var(--sky) 0%, transparent 45%),
      linear-gradient(160deg, #f6a6c8, var(--maroon));
    border: 6px solid var(--white);
  }
</style>
</head>
<body>
  <main class="flyer">
    <div class="studio-name">Meridian Dance Studio LLC</div>
    <div class="title-band"></div>
    <div class="title-rule"></div>
    <h1 class="theme-title">STEP INTO STARLIGHT...</h1>
    <p class="recital-line">FOR MY <span class="edition">6TH</span> ANNUAL RECITAL</p>
    <div class="details">
      <p>DATE: JUNE 24, 2017</p>
      <p>TIME: 2 PM &amp; 7 PM</p>
    </div>
    <div class="venue-rule"></div>
    <div class="venue-band">
      <p class="venue-name">LOCATION: PINECREST HOLLOW HIGH SCHOOL</p>
      <p class="venue-address">418 MARLOW RD, ASHFORD CHARTER TWP, MI 48612</p>
    </div>
    <div class="dancer-art" role="img" aria-label="Illustration of a leaping dancer over pink and teal swirls with maroon paint splatter"></div>
  </main>
</body>
</html>
```